Business needs Office Posters Designed

I need a office poster designed to put on a 2 feet x 3 feet space:
My Employee is Better Than Me.
- to signify the importance of listening to your employees, because they know better, more experienced in their respective fields.

Target Market(s)

employees

Industry/Entity Type

Healthcare

```html
<!DOCTYPE html>
<html lang="en">
<head>
<meta charset="UTF-8">
<title>My Employee Is Better Than Me — Office Poster</title>
<link rel="stylesheet" href="https://fonts.googleapis.com/css2?family=Oswald:wght@700&display=swap">
<style>
  :root {
    --backdrop: #e9eaea;
    --paper: #ffffff;
    --headline-violet: #7a75b5;
    --headline-charcoal: #414042;
    --crowd-dark: #3a302c;
    --crowd-mid: #6b5648;
    --crowd-warm: #9a7a5e;
  }

  * { margin: 0; padding: 0; box-sizing: border-box; }

  html, body {
    width: 960px;
    height: 1200px;
    overflow: hidden;
    background: var(--backdrop);
  }

  .canvas {
    position: relative;
    width: 960px;
    height: 1200px;
    display: flex;
    align-items: center;
    justify-content: center;
  }

  .poster {
    position: relative;
    width: 760px;
    height: 1140px;
    background: var(--paper);
    box-shadow: 0 2px 12px rgba(0, 0, 0, 0.12);
  }

  .poster__illustration {
    position: absolute;
    left: 50px;
    top: 60px;
    width: 660px;
    height: 560px;
  }

  .poster__illustration svg {
    display: block;
    width: 100%;
    height: 100%;
  }

  .headline {
    position: absolute;
    left: 0;
    right: 0;
    top: 640px;
    text-align: center;
    font-family: "Oswald", "Arial Narrow", sans-serif;
    font-weight: 700;
    text-transform: uppercase;
    color: var(--headline-violet);
    line-height: 0.98;
    letter-spacing: -1px;
  }

  .headline__line { display: block; }
  .headline__line--lead { font-size: 92px; }
  .headline__line--main { font-size: 150px; }
  .headline__accent { color: var(--headline-charcoal); }
</style>
</head>
<body>
  <main class="canvas">
    <article class="poster">
      <div class="poster__illustration" role="img" aria-label="Aerial view of a large crowd of people gathered to form the silhouette of a flexing strong man">
        <svg viewBox="0 0 660 560" xmlns="http://www.w3.org/2000/svg" aria-hidden="true">
          <defs>
            <radialGradient id="crowd-tone" cx="50%" cy="45%" r="60%">
              <stop offset="0%" stop-color="var(--crowd-mid)"/>
              <stop offset="70%" stop-color="var(--crowd-dark)"/>
              <stop offset="100%" stop-color="var(--crowd-warm)"/>
            </radialGradient>
          </defs>
          <rect x="20" y="40" width="620" height="500" rx="30" fill="url(#crowd-tone)" opacity="0.85"/>
        </svg>
      </div>

      <h1 class="headline">
        <span class="headline__line headline__line--lead">My Employee</span>
        <span class="headline__line headline__line--main">Is Better</span>
        <span class="headline__line headline__line--main">Than <span class="headline__accent">Me</span></span>
      </h1>
    </article>
  </main>
</body>
</html>
```